Stainless Steel Business Card

I have a fiber laser and want to highlight its capabilities in a business card. On the card I want

Brevik Industries
Martin Brevik
martin@mbrevik-mail.net
417-555-0163

This will be cut / engraved on stainless steel. I want the Brevik Industries to be prominent with laser cut font so that there are no dropouts on the O and A's. My name email and phone number should be engraved black. I would like some cool geometric patterns to cutout on the card to highlight the capabilities of my machine. I will need to files in the end either SVG or dxf of the engrave portion and the cut portion.

```html
<!DOCTYPE html>
<html lang="en">
<head>
<meta charset="utf-8">
<title>Brevik Industries – Stainless Steel Business Card</title>
<link rel="stylesheet" href="https://fonts.googleapis.com/css2?family=Allerta+Stencil&family=Montserrat:wght@400;500&display=swap">
<style>
  :root {
    --page-bg: #e4e3e1;
    --steel-dark: #3f4042;
    --steel-mid: #4b4c4e;
    --steel-light: #56575a;
    --edge: #9a9b9d;
    --cut-edge: #b9babc;
    --engrave-light: #d9d9d8;
    --engrave-black: #141414;
  }
  html, body {
    margin: 0;
    width: 1200px;
    height: 728px;
    overflow: hidden;
    background: var(--page-bg);
    font-family: "Montserrat", Arial, sans-serif;
  }
  .stage {
    width: 1200px;
    height: 728px;
    display: flex;
    align-items: center;
    justify-content: center;
  }
  .card {
    position: relative;
    width: 1000px;
    height: 572px;
    border-radius: 26px;
    box-sizing: border-box;
    border: 2px solid var(--edge);
    background:
      repeating-linear-gradient(180deg, rgba(255,255,255,0.025) 0 2px, rgba(0,0,0,0.03) 2px 5px),
      linear-gradient(100deg, var(--steel-dark), var(--steel-light) 45%, var(--steel-mid) 70%, var(--steel-dark));
    text-align: center;
  }
  .cutouts {
    position: absolute;
    inset: 0;
    width: 996px;
    height: 568px;
  }
  .cutout {
    fill: var(--page-bg);
    stroke: var(--cut-edge);
    stroke-width: 1.5;
    stroke-linejoin: round;
  }
  .company-name {
    position: absolute;
    top: 96px;
    left: 0;
    right: 0;
    margin: 0;
    font-family: "Allerta Stencil", "Montserrat", sans-serif;
    font-size: 66px;
    font-weight: 400;
    letter-spacing: 6px;
    line-height: 1;
    color: var(--engrave-light);
  }
  .company-sub {
    position: absolute;
    top: 182px;
    left: 0;
    right: 0;
    margin: 0;
    font-family: "Allerta Stencil", "Montserrat", sans-serif;
    font-size: 24px;
    letter-spacing: 3px;
    line-height: 1;
    color: var(--engrave-light);
  }
  .rule {
    position: absolute;
    left: 90px;
    right: 90px;
    height: 3px;
    background: var(--engrave-light);
    border-radius: 2px;
  }
  .rule--top { top: 240px; }
  .rule--bottom { top: 390px; }
  .person-name {
    position: absolute;
    top: 290px;
    left: 0;
    right: 0;
    margin: 0;
    font-size: 50px;
    font-weight: 500;
    line-height: 1;
    color: var(--engrave-black);
  }
  .contact-row {
    position: absolute;
    top: 450px;
    left: 0;
    right: 0;
    display: flex;
    justify-content: center;
    align-items: center;
    gap: 44px;
    font-size: 31px;
    font-weight: 500;
    color: var(--engrave-black);
  }
  .contact-item {
    display: flex;
    align-items: center;
    gap: 14px;
  }
  .contact-icon { width: 40px; height: 40px; display: block; }
</style>
</head>
<body>
<main class="stage">
  <article class="card">
    <svg class="cutouts" viewBox="0 0 996 568" aria-hidden="true">
      <g class="cutout-group cutout-group--top-left">
        <polygon class="cutout" points="36,36 66,36 51,62"/>
        <polygon class="cutout" points="72,36 102,36 87,62"/>
        <polygon class="cutout" points="108,36 138,36 123,62"/>
        <polygon class="cutout" points="54,68 84,68 69,94"/>
        <polygon class="cutout" points="90,68 120,68 105,94"/>
        <polygon class="cutout" points="72,100 102,100 87,126"/>
      </g>
      <g class="cutout-group cutout-group--top-right">
        <polygon class="cutout" points="960,36 930,36 945,62"/>
        <polygon class="cutout" points="924,36 894,36 909,62"/>
        <polygon class="cutout" points="888,36 858,36 873,62"/>
        <polygon class="cutout" points="942,68 912,68 927,94"/>
        <polygon class="cutout" points="906,68 876,68 891,94"/>
        <polygon class="cutout" points="924,100 894,100 909,126"/>
      </g>
      <g class="cutout-group cutout-group--bottom-left">
        <polygon class="cutout" points="36,532 66,532 51,506"/>
        <polygon class="cutout" points="72,532 102,532 87,506"/>
        <polygon class="cutout" points="54,500 84,500 69,474"/>
      </g>
      <g class="cutout-group cutout-group--bottom-right">
        <polygon class="cutout" points="960,532 930,532 945,506"/>
        <polygon class="cutout" points="924,532 894,532 909,506"/>
        <polygon class="cutout" points="942,500 912,500 927,474"/>
      </g>
    </svg>
    <h1 class="company-name">BREVIK</h1>
    <p class="company-sub">INDUSTRIES</p>
    <div class="rule rule--top"></div>
    <p class="person-name">Martin Brevik</p>
    <div class="rule rule--bottom"></div>
    <div class="contact-row">
      <span class="contact-item">
        <svg class="contact-icon" viewBox="0 0 40 40" aria-hidden="true">
          <rect x="1" y="1" width="38" height="38" rx="6" fill="var(--engrave-black)"/>
          <rect x="8" y="11" width="24" height="18" rx="1.5" fill="none" stroke="var(--steel-light)" stroke-width="2.2"/>
          <path d="M8 12 L20 22 L32 12" fill="none" stroke="var(--steel-light)" stroke-width="2.2" stroke-linejoin="round"/>
        </svg>
        <span class="contact-email">martin@mbrevik-mail.net</span>
      </span>
      <span class="contact-item">
        <svg class="contact-icon" viewBox="0 0 40 40" aria-hidden="true">
          <rect x="1" y="1" width="38" height="38" rx="6" fill="var(--engrave-black)"/>
          <path d="M14 8 C12 8 10 10 10.5 13 C12 22 18 29 27 31 C30 31.5 32 29 32 27 L28 23.5 L24.5 25.5 C21 23.5 17.5 20 16 16 L18 12.5 Z" fill="var(--steel-light)"/>
        </svg>
        <span class="contact-phone">417-555-0163</span>
      </span>
    </div>
  </article>
</main>
</body>
</html>
```